Business Card Design

We like to use greens as you will see in our logo (but not TOO much green). We are a Dental Clinic in a somewhat eccentric community. We do not like the dated sharp designs which we see many dentists use. We're looking for something bright and fresh while still maintaining the integrity of the profession. Elegance is not necessarily what we are going for... we need for the design to be "mature" but also up-lifting.

See our logo.
Updates

Project Deadline Extended
Reason: We have 5 designs which we like. But we'd like to see a few more before committing to a design.

Project Deadline Extended
Reason: We are awaiting revisions to this project. We are still welcoming designs while we wait to see if designers are able to provide to us the revisions we require in order to proceed with a selection.

Target Market(s)

Younger families - ages late 20's to early 40's

Industry/Entity Type

Business

Contact Information for Business Card

Marlow T. Benning DDS 2740 W. Hollister Rd. Ste. 7 Elmbrook, ST 48133 (555)555-0193 FX (555)555-0147 info@BrightwellDentalCareMi.example BrigthwellDentalCareMi.example on the back of the card we need an appointment reminder (For____ Date___ Time____) with "If you are unable to keep your appointment, kindly give 48 hours notice" at the bottom. No use of teeth in the design. DOUBLE SIDED DESIGN

Requirements
Should not have
• The use of pictures of teeth

```html
<!DOCTYPE html>
<html lang="en">
<head>
<meta charset="utf-8">
<title>Brightwell Dental Care – Business Card</title>
<link rel="stylesheet" href="https://fonts.googleapis.com/css2?family=Open+Sans:ital,wght@0,400;0,600;0,700;1,400&family=Marcellus&display=swap">
<style>
  :root {
    --green-deep: #1e6b34;
    --green-brand: #2a7a3b;
    --ink: #2b2b2b;
    --ink-soft: #4a4a4a;
    --rule: #9a9a9a;
    --card: #ffffff;
    --backdrop: #ece8e2;
  }
  * { box-sizing: border-box; margin: 0; padding: 0; }
  html, body { width: 1200px; height: 1183px; overflow: hidden; }
  body {
    background: var(--backdrop);
    font-family: "Open Sans", Arial, sans-serif;
    color: var(--ink);
    position: relative;
  }
  .card {
    position: absolute;
    background: var(--card);
    box-shadow: 0 2px 8px rgba(0,0,0,.18);
    overflow: hidden;
  }

  /* ---------- Front ---------- */
  .card--front { left: 35px; top: 42px; width: 936px; height: 537px; }
  .side-tab {
    position: absolute; top: 96px; width: 20px; height: 358px;
    background: var(--green-deep);
  }
  .side-tab--left { left: 0; border-radius: 0 14px 14px 0; }
  .side-tab--right { right: 0; border-radius: 14px 0 0 14px; }

  .brand {
    position: absolute; display: flex; align-items: center;
    color: var(--green-brand); font-weight: 600;
  }
  .brand__dot { border-radius: 50%; background: var(--green-brand); flex: none; }
  .brand__name { line-height: 1.05; white-space: nowrap; }
  .brand__name span { display: block; letter-spacing: 1px; }

  .brand--front { left: 40px; top: 215px; gap: 14px; }
  .brand--front .brand__dot { width: 28px; height: 28px; }
  .brand--front .brand__name { font-size: 62px; }
  .brand--front .brand__name span { font-size: 45px; }

  .divider {
    position: absolute; left: 501px; top: 92px; width: 2px; height: 357px;
    background: var(--rule);
  }
  .contact { position: absolute; left: 523px; top: 96px; }
  .contact__name { font-size: 31px; font-weight: 700; color: var(--green-deep); line-height: 1.2; }
  .contact__title { font-size: 24px; color: var(--ink-soft); line-height: 1.3; margin-bottom: 38px; }
  .contact__list { list-style: none; }
  .contact__list li {
    display: flex; align-items: center; gap: 7px;
    font-size: 18.5px; height: 41.5px; color: var(--ink);
  }
  .contact__list svg { width: 17px; height: 17px; flex: none; fill: var(--green-deep); }
  .contact__address { margin-top: 24px; font-size: 19.5px; line-height: 1.5; color: var(--ink); }

  /* ---------- Back ---------- */
  .card--back { left: 228px; top: 615px; width: 942px; height: 536px; }
  .brand--back { left: 76px; top: 30px; gap: 10px; }
  .brand--back .brand__dot { width: 20px; height: 20px; }
  .brand--back .brand__name { font-size: 40px; }
  .brand--back .brand__name span { font-size: 29px; }

  .appointment__title {
    position: absolute; left: 76px; top: 172px;
    font-family: "Marcellus", Georgia, serif; font-size: 36px; font-weight: 400;
    color: var(--green-deep); letter-spacing: .5px;
  }
  .field { position: absolute; font-size: 24px; color: var(--ink-soft); line-height: 1; }
  .fill-line { position: absolute; height: 0; border-bottom: 2px dotted #7a7a7a; }
  .field-box {
    position: absolute; width: 168px; height: 35px;
    border: 2px solid var(--ink-soft); border-radius: 3px;
  }

  .weekdays { position: absolute; right: 28px; top: 0; width: 260px; height: 100%; }
  .weekday { position: absolute; right: 0; display: flex; align-items: center; gap: 14px; }
  .weekday__label { font-weight: 700; font-size: 24px; color: var(--ink-soft); }
  .weekday__box { width: 58px; height: 34px; border: 2px solid var(--ink-soft); border-radius: 3px; }

  .notice {
    position: absolute; left: 79px; right: 32px; top: 463px;
    font-style: italic; font-size: 24px; color: var(--ink); white-space: nowrap;
  }
  .base-band {
    position: absolute; left: 0; right: 0; bottom: 0; height: 15px;
    background: var(--green-deep);
  }
</style>
</head>
<body>

<section class="card card--front" aria-label="Business card front">
  <div class="side-tab side-tab--left"></div>
  <div class="side-tab side-tab--right"></div>

  <div class="brand brand--front">
    <div class="brand__dot"></div>
    <div class="brand__name">Brightwell<span>DENTAL CARE</span></div>
  </div>

  <div class="divider"></div>

  <div class="contact">
    <div class="contact__name">Marlow T. Benning</div>
    <div class="contact__title">DDS</div>
    <ul class="contact__list">
      <li>
        <svg viewBox="0 0 24 24" aria-hidden="true"><path d="M6.6 10.8a15.1 15.1 0 0 0 6.6 6.6l2.2-2.2c.3-.3.7-.4 1-.2 1.1.4 2.3.6 3.6.6.6 0 1 .4 1 1V20c0 .6-.4 1-1 1A17 17 0 0 1 3 4c0-.6.4-1 1-1h3.5c.6 0 1 .4 1 1 0 1.3.2 2.5.6 3.6.1.3 0 .7-.2 1z"/></svg>
        (555)555-0193
      </li>
      <li>
        <svg viewBox="0 0 24 24" aria-hidden="true"><path d="M7 3h10v5H7zM4 9h16a2 2 0 0 1 2 2v6h-4v4H6v-4H2v-6a2 2 0 0 1 2-2zm4 7v3h8v-3z"/></svg>
        (555)555-0147
      </li>
      <li>
        <svg viewBox="0 0 24 24" aria-hidden="true"><path d="M3 5h18v14H3zm2 2v.5l7 5 7-5V7l-7 5z"/></svg>
        info@BrightwellDentalCareMi.example
      </li>
      <li>
        <svg viewBox="0 0 24 24" aria-hidden="true"><path d="M12 2a10 10 0 1 0 0 20 10 10 0 0 0 0-20zm6.9 6h-3a15 15 0 0 0-1.3-3.9A8 8 0 0 1 18.9 8zM12 4c.8 1.1 1.5 2.5 1.9 4h-3.8c.4-1.5 1.1-2.9 1.9-4zM4.3 14a8 8 0 0 1 0-4h3.4a16 16 0 0 0 0 4zm.8 2h3a15 15 0 0 0 1.3 3.9A8 8 0 0 1 5.1 16zm3-8h-3a8 8 0 0 1 4.3-3.9A15 15 0 0 0 8.1 8zM12 20c-.8-1.1-1.5-2.5-1.9-4h3.8c-.4 1.5-1.1 2.9-1.9 4zm2.3-6H9.7a14 14 0 0 1 0-4h4.6a14 14 0 0 1 0 4zm.3 5.9a15 15 0 0 0 1.3-3.9h3a8 8 0 0 1-4.3 3.9zm1.7-5.9a16 16 0 0 0 0-4h3.4a8 8 0 0 1 0 4z"/></svg>
        BrigthwellDentalCareMi.example
      </li>
    </ul>
    <p class="contact__address">2740 W. Hollister Rd.<br>Ste. 7 Elmbrook, ST 48133</p>
  </div>
</section>

<section class="card card--back" aria-label="Business card back, appointment reminder">
  <div class="brand brand--back">
    <div class="brand__dot"></div>
    <div class="brand__name">Brightwell<span>DENTAL CARE</span></div>
  </div>

  <h2 class="appointment__title">YOUR APPOINTMENT</h2>

  <span class="field" style="left:82px; top:257px;">Name :</span>
  <div class="fill-line" style="left:189px; width:522px; top:276px;"></div>

  <span class="field" style="left:82px; top:326px;">Date :</span>
  <div class="fill-line" style="left:189px; width:170px; top:345px;"></div>
  <span class="field" style="left:370px; top:326px;">Time :</span>
  <div class="fill-line" style="left:448px; width:162px; top:345px;"></div>
  <span class="field" style="left:614px; top:326px;">am / pm</span>

  <span class="field" style="left:82px; top:391px;">Next Appointment</span>
  <div class="field-box" style="left:335px; top:385px;"></div>
  <div class="field-box" style="left:543px; top:385px;"></div>

  <div class="weekdays">
    <div class="weekday" style="top:79px;"><span class="weekday__label">MON</span><span class="weekday__box"></span></div>
    <div class="weekday" style="top:143px;"><span class="weekday__label">TUE</span><span class="weekday__box"></span></div>
    <div class="weekday" style="top:208px;"><span class="weekday__label">WED</span><span class="weekday__box"></span></div>
    <div class="weekday" style="top:276px;"><span class="weekday__label">THU</span><span class="weekday__box"></span></div>
    <div class="weekday" style="top:334px;"><span class="weekday__label">FRI</span><span class="weekday__box"></span></div>
    <div class="weekday" style="top:390px;"><span class="weekday__label">SAT</span><span class="weekday__box"></span></div>
  </div>

  <p class="notice">If you are unable to keep your appointment, kindly give 48 hours notice</p>
  <div class="base-band"></div>
</section>

</body>
</html>
```